I need a design for Corvane Homes which is a custom home builder. The name on it will be Dan Hartley, and I will give the phone number to the winning design. No address or website needed.

```html
<!DOCTYPE html>
<html lang="en">
<head>
<meta charset="UTF-8">
<title>Corvane Homes – Business Card</title>
<link href="https://fonts.googleapis.com/css2?family=Libre+Baskerville:wght@400;700&display=swap" rel="stylesheet">
<style>
  :root {
    --navy: #1f1d6b;
    --royal: #3a36c9;
    --violet: #5a55e0;
    --slate: #9a9aa6;
    --silver: #c9c9d1;
    --card: #ffffff;
    --backdrop: #e6e6ea;
  }
  * { margin: 0; padding: 0; box-sizing: border-box; }
  html, body {
    width: 789px;
    height: 1200px;
    overflow: hidden;
    background: var(--backdrop);
    font-family: "Libre Baskerville", "Times New Roman", serif;
  }
  .canvas {
    width: 789px;
    height: 1200px;
    display: flex;
    flex-direction: column;
    align-items: center;
    justify-content: center;
    gap: 80px;
  }
  .card {
    position: relative;
    width: 640px;
    height: 366px;
    background: var(--card);
    box-shadow: 0 10px 28px rgba(20, 20, 60, 0.18);
    overflow: hidden;
  }
  .card-front .brand-band {
    position: absolute;
    left: 0;
    top: 42px;
    width: 100%;
    height: 58px;
    background: var(--navy);
    display: flex;
    align-items: center;
    padding-left: 40px;
  }
  .brand-name {
    color: #ffffff;
    font-weight: 700;
    font-size: 30px;
    letter-spacing: 0.2px;
  }
  .contact {
    position: absolute;
    left: 40px;
    top: 150px;
    color: var(--navy);
  }
  .contact-name {
    font-size: 44px;
    font-weight: 400;
    line-height: 1.15;
  }
  .contact-phone {
    font-size: 36px;
    font-weight: 400;
    line-height: 1.2;
  }
  .accent-cluster {
    position: absolute;
    right: 0;
    bottom: 0;
    width: 200px;
    height: 266px;
  }
  .pattern-field {
    position: absolute;
    inset: 0;
    width: 100%;
    height: 100%;
  }
</style>
</head>
<body>
  <main class="canvas">
    <section class="card card-front">
      <div class="brand-band">
        <span class="brand-name">Corvane Homes</span>
      </div>
      <div class="contact">
        <p class="contact-name">Dan Hartley</p>
        <p class="contact-phone">404.555.0192</p>
      </div>
      <svg class="accent-cluster" viewBox="0 0 200 266" role="img" aria-label="Geometric cluster of blue, navy and grey triangles">
        <defs>
          <linearGradient id="clusterTone" x1="0" y1="0" x2="1" y2="1">
            <stop offset="0" stop-color="var(--silver)"/>
            <stop offset="0.45" stop-color="var(--violet)"/>
            <stop offset="1" stop-color="var(--navy)"/>
          </linearGradient>
        </defs>
        <polygon points="200,0 200,266 40,266" fill="url(#clusterTone)"/>
      </svg>
    </section>

    <section class="card card-back">
      <svg class="pattern-field" viewBox="0 0 640 366" role="img" aria-label="All-over mosaic of blue, navy and grey triangles">
        <defs>
          <linearGradient id="mosaicTone" x1="0" y1="0" x2="1" y2="1">
            <stop offset="0" stop-color="var(--violet)"/>
            <stop offset="0.4" stop-color="var(--royal)"/>
            <stop offset="0.7" stop-color="var(--slate)"/>
            <stop offset="1" stop-color="var(--navy)"/>
          </linearGradient>
        </defs>
        <rect width="640" height="366" fill="url(#mosaicTone)"/>
      </svg>
    </section>
  </main>
</body>
</html>
```